普段のお店は入りづらい雰囲気になっています。一部の時間のみ、色々な方が入りやすいような雰囲気を作るために目立つのぼりを立てたいです

BARとしてのお店のイメージもありますので、居酒屋さんのようなのぼりではなく、Barらしさが出ていると良いなと思います。

ハッピーアワーの文字が一番目立つように(カタカナ、英語どちらでも)。時間も載せたいところですが、変更するかもしれないので今回は載せなくて構いません。店名とロゴ、ビールは瓶ビールなので、瓶ビールやワイン、カクテル(ロングカクテル)などのイラスト等と、カクテル¥500 ウイスキー半額というフレーズを載せて頂きたいです。

色味は指定していますが、白黒グレー系でも目立つ感じであれば構いません。
一目でわかりやすいものを希望します。

メニュー等の詳細は別で看板を出す予定でいます。
店名 KEDU

シンプル 複雑
単色 カラフル
暗い 明るい
日常 高級
遊び心 厳粛
未来的 伝統的
女性的 男性的
赤系、黄・オレンジ系、茶系
のぼり自体はヒモトヤに入稿して注文する予定です。
レギュラーサイズの左側・縦 1800×600

以前こちらでお願いした際に、データファイルのやり取りで時間をとられたことがあります。なのでヒモトヤに簡単にデータ入稿出来るものを頂きたいです。

素人ですので、その辺了承して下さる方にお願いしたいと思います。
(とはいえ、最低限普通の事は分かりますので大丈夫です)

のぼりを置く場所も添付します。ビルの入り口付近(同じような雰囲気で2方向あります)に何個かずつ立てる予定でいます。
ご希望がありましたので、aiのロゴデータを追加します
載せて頂きたい文言につきましては、選ばせて頂いた方に内容の変更をお願いするかと思います。
よろしくお願い致します。

男女ともに入りやすいイメージを持っていただけるのでは、と思いました。
お酒の画像もパッと見た感じ分かりやすく、カジュアル感、Barらしさも出ていてよかったです。

たくさんの方から応募を頂き、スタッフの意見も聞きつつ、悩んだ上で一つを選ばせて頂きました。
お店の事を色々な方に一緒に考えて頂き有り難かったです。
また今後もお世話になると思いますので、その際にはよろしくお願い致します。
ありがとうございました。

```html
<!DOCTYPE html>
<html lang="ja">
<head>
<meta charset="utf-8">
<title>KEDU Happy Hour Nobori</title>
<link href="https://fonts.googleapis.com/css2?family=Oswald:wght@600;700&family=Noto+Sans+JP:wght@700;900&display=swap" rel="stylesheet">
<style>
  :root{
    --bar-red:#a5241d;
    --cream:#fdf2c2;
    --white:#ffffff;
    --page:#ffffff;
    --bottle-top:#7a3b16;
    --bottle-bottom:#c9832f;
    --glass-a:#f4c463;
    --glass-b:#b9d98a;
  }
  *{margin:0;padding:0;box-sizing:border-box}
  html,body{width:1200px;height:2400px;overflow:hidden;background:var(--page)}
  .flag{
    position:absolute;left:210px;top:75px;width:780px;height:2250px;
    background:var(--bar-red);overflow:hidden;
    font-family:"Noto Sans JP",sans-serif;
  }
  .brand{
    position:absolute;top:80px;left:0;width:100%;height:120px;
    display:flex;align-items:center;justify-content:center;gap:26px;
    color:var(--white);
  }
  .brand-mark{width:52px;height:52px;background:var(--white)}
  .brand-name{font-family:"Oswald",sans-serif;font-weight:600;font-size:96px;letter-spacing:12px;line-height:1}
  .headline{
    position:absolute;left:60px;color:var(--white);white-space:nowrap;
    font-family:"Oswald",sans-serif;font-weight:700;font-size:250px;line-height:1;
    transform:scaleX(0.86);transform-origin:left top;
  }
  .headline-happy{top:205px}
  .headline-hour{top:470px}
  .bottle-art{
    position:absolute;left:610px;top:560px;width:90px;height:300px;
    border-radius:36px 36px 12px 12px;
    background:linear-gradient(180deg,var(--bottle-top),var(--bottle-bottom));
    transform:rotate(14deg);
  }
  .offer-panel{
    position:absolute;left:32px;right:37px;top:895px;height:965px;
    background:var(--cream);
  }
  .offer-label,.offer-value{
    position:absolute;left:50px;color:var(--bar-red);font-weight:900;line-height:1;white-space:nowrap;
  }
  .cocktail-label{top:70px;font-size:105px}
  .cocktail-price{top:220px;font-size:195px;letter-spacing:-4px}
  .offer-divider{position:absolute;left:0;right:0;top:490px;height:14px;background:var(--bar-red)}
  .whisky-label{top:560px;font-size:90px}
  .whisky-value{top:690px;font-size:215px}
  .glasses-art{
    position:absolute;right:0;top:30px;width:165px;height:820px;
    background:linear-gradient(180deg,var(--glass-a),var(--glass-b) 45%,var(--glass-a));
    border-radius:20px 0 0 20px;
  }
  .weekend-only{
    position:absolute;top:1880px;left:0;width:100%;text-align:center;
    color:var(--white);font-weight:900;font-size:150px;line-height:1.2;letter-spacing:4px;
  }
</style>
</head>
<body>
  <div class="flag">
    <div class="brand">
      <span class="brand-mark"></span>
      <span class="brand-name">KEDU</span>
    </div>
    <div class="headline headline-happy">HAPPY</div>
    <div class="headline headline-hour">HOUR</div>
    <div class="bottle-art" role="img" aria-label="瓶ビールのイラスト"></div>

    <div class="offer-panel">
      <div class="offer-label cocktail-label">カクテル</div>
      <div class="offer-value cocktail-price">¥500</div>
      <div class="offer-divider"></div>
      <div class="offer-label whisky-label">ウイスキー</div>
      <div class="offer-value whisky-value">半額</div>
      <div class="glasses-art" role="img" aria-label="ロングカクテルとウイスキーグラスのイラスト"></div>
    </div>

    <div class="weekend-only">週末限定</div>
  </div>
</body>
</html>
```